"Velvet Harbor Tides" book cover design

PLEASE READ THE SHOULD NOT HAVES. DO NOT USE THE IMAGE I PROVIDED FOR THE KEYHOLE. I JUST PULLED THAT OFF TROVIX TO SHOW AN EXAMPLE.

Front cover sketch is supposed to be a keyhole on a doorway. I’m picturing and older, more rustic/weathered wood and keyhole.

Hoping the back cover can be a reversed, mirror image of the front with an eye peeking through the exact same keyhole.

I don't have the book edited and formatted yet, but based on my other books' word and page count at 5.25x8, this one should come out to about 375 pages (to keep in mind for spine width).

Here is the back cover summary:

From awkward virgin to male entertainer to a spell of chastity, Velvet Harbor Tides traces a coming-of-age story fueled by the power of psychedelics. These tales tumble down a rabbit hole of life’s dualities—ranging from addiction to sobriety, philandering to celibacy, narcissism to spiritualism, and atheism to meeting God. Both the darkest corners of the human psyche and the lightest experiences of existential bliss are explored in this winding series. These musings highlight the wisdom gained from experimentation with LSD and Psilocybin.

Psychedelics are a trowel that digs deep into the soil of the soul, unearthing experiences beyond imagination. You hold in your hands a collection of the most important lessons learned by an explorer who delved into varying degrees of this otherworldly consciousness roughly a hundred times over five years. Whether these recollections were spiritual occurrences induced by a higher power or just convincing hallucinations brought on by a chemical power doesn’t matter. The trips were often more real than any occurrence on the sober plane of existence and pivotal in shaping one man’s worldview.

Target Market(s)

Community interested in psychedelics, mushrooms, LSD, spiritual healing, trauma healing, spiritual experience, etc.

Font styles to use
Other font styles liked:
• Times New Roman for the back summary

Requirements
Must have
• 5.25x8, formatted for upload on Brellon QPR
Nice to have
• I'm hoping the font for the title and “Anonymous” can look like someone carved them into the door, like you would names on a tree.
Should not have
• No AI generated images preferred. Also, the images I provided were pulled off Trovix for inspiration, but should not be used in your design.

```html
<!DOCTYPE html>
<html lang="en">
<head>
<meta charset="utf-8">
<title>Velvet Harbor Tides — Front Cover</title>
<link href="https://fonts.googleapis.com/css2?family=Cinzel:wght@600;700&display=swap" rel="stylesheet">
<style>
  :root {
    --backdrop: #f4e9bf;
    --wood-dark: #2a1c14;
    --wood-mid: #3b2a1e;
    --wood-light: #4a3526;
    --grain: rgba(20, 12, 8, 0.35);
    --carved-gold: #ead9a4;
    --carved-shade: #1a110b;
    --rust: #8a4a26;
    --rust-dark: #5e2c16;
    --scene-violet: #3a2a6b;
    --scene-night: #120f2a;
    --scene-teal: #2f8fb0;
    --scene-amber: #d08a4a;
  }

  * { margin: 0; padding: 0; box-sizing: border-box; }

  html, body {
    width: 1200px;
    height: 1200px;
    overflow: hidden;
    background: var(--backdrop);
  }

  .canvas {
    position: relative;
    width: 1200px;
    height: 1200px;
  }

  .cover {
    position: absolute;
    left: 272px;
    top: 100px;
    width: 656px;
    height: 1000px;
    background:
      repeating-linear-gradient(90deg,
        transparent 0 23px,
        var(--grain) 23px 25px,
        transparent 25px 61px,
        rgba(20,12,8,0.2) 61px 62px,
        transparent 62px 97px),
      linear-gradient(90deg, var(--wood-dark) 0%, var(--wood-mid) 30%, var(--wood-light) 55%, var(--wood-mid) 80%, var(--wood-dark) 100%);
    overflow: hidden;
  }

  .cover-title,
  .cover-author {
    position: absolute;
    left: 0;
    width: 100%;
    text-align: center;
    font-family: "Cinzel", "Times New Roman", serif;
    font-weight: 700;
    color: var(--carved-gold);
    text-shadow:
      -1px -1px 0 var(--carved-shade),
      2px 2px 2px rgba(0,0,0,0.55);
  }

  .cover-title {
    top: 78px;
    font-size: 60px;
    line-height: 1.12;
    letter-spacing: 1px;
  }

  .cover-author {
    top: 880px;
    font-size: 52px;
    letter-spacing: 1px;
  }

  .keyhole {
    position: absolute;
    left: 0;
    top: 0;
    width: 656px;
    height: 1000px;
  }
</style>
</head>
<body>
  <main class="canvas">
    <section class="cover" aria-label="Front cover">
      <h1 class="cover-title">VELVET HARBOR<br>TIDES</h1>

      <svg class="keyhole" viewBox="0 0 656 1000" aria-hidden="false">
        <defs>
          <linearGradient id="keyhole-scene" x1="0" y1="0" x2="0" y2="1">
            <stop offset="0" stop-color="var(--scene-violet)"/>
            <stop offset="0.4" stop-color="var(--scene-night)"/>
            <stop offset="0.75" stop-color="var(--scene-teal)"/>
            <stop offset="1" stop-color="var(--scene-amber)"/>
          </linearGradient>
        </defs>
        <path class="keyhole-rim"
              d="M 243 503.6 A 150 150 0 1 1 413 503.6 L 488 848 L 168 848 Z"
              fill="none" stroke="var(--rust-dark)" stroke-width="30" stroke-linejoin="round"/>
        <path class="keyhole-opening" role="img"
              aria-label="View through the keyhole: a lone traveller on a winding path through a glowing psychedelic forest at night"
              d="M 243 503.6 A 150 150 0 1 1 413 503.6 L 488 848 L 168 848 Z"
              fill="url(#keyhole-scene)" stroke="var(--rust)" stroke-width="14" stroke-linejoin="round"/>
      </svg>

      <p class="cover-author">ANONYMOUS</p>
    </section>
  </main>
</body>
</html>
```